International Travel & Visas Firm needs a Schengen Visa eBook Cover Design

We need an ebook cover design for an online based travel, immigration, visas & nationality law firm called 'OrV' (ordinance and relocation). We are all about helping people overcome the obstacles to travel and ensuring that people achieve their dreams and ambitions through travel to various destinations and bettering their lives.This initial ebook cover is for our downloaded pdf ebook all about Schengen visas and travelling to any of the 26 European countries that form the Schengen Zone.We want people to be excited about buying this book even before receiving it.We would like to see amazing designs that also speak to our logo and new branding.Check out https://ordinanceandrelocation.example/schengen-visas/ and http://ordinanceandrelocation.pages.funnelkit.example/start-your-schengen-visa-application

Target Market(s)

Travellers that want to get a visa to travel around Europe

Industry/Entity Type

Travel Industry

Colors
fbee3d
faa54b

Requirements
Must have
• - Title:
• Schengen Visa Guide
Nice to have
• - tagline:
• Liberate yourself and travel to 26 European Countries
• - OrV Logo
• - Reference to it being an insider's guide to Schengen Visas
• - a play on the word OrV (I am)

```html
<!DOCTYPE html>
<html lang="en">
<head>
<meta charset="utf-8">
<title>Schengen Visa Guide – eBook Cover Spread</title>
<link rel="stylesheet" href="https://fonts.googleapis.com/css2?family=Raleway:wght@300;400;700&display=swap">
<style>
  :root {
    --orange: #f9a34b;
    --yellow: #f9ec3d;
    --charcoal: #4d4d4d;
    --ink: #474747;
    --photo-dark: #1c1c1c;
    --photo-mid: #555555;
    --photo-light: #9a9a9a;
    --paper: #ffffff;
    --edge: #ececec;
  }
  html, body {
    margin: 0;
    padding: 0;
    width: 1200px;
    height: 1200px;
    overflow: hidden;
    background: var(--paper);
  }
  .cover-spread {
    display: block;
    width: 1200px;
    height: 1200px;
    font-family: "Raleway", sans-serif;
  }
  .page-edge { fill: var(--paper); stroke: var(--edge); stroke-width: 1.5; }
  .orange-wedge { fill: var(--orange); }
  .yellow-band { fill: var(--yellow); }
  .footer-bar { fill: var(--charcoal); }
  .spine-fold { stroke: #6a6a6a; stroke-width: 1.5; }
  .accent-square { fill: var(--orange); }
  .title-main { font-weight: 700; font-size: 72px; fill: var(--ink); }
  .title-sub { font-weight: 300; font-size: 52px; fill: var(--ink); }
  .tagline, .insider-note { font-weight: 400; font-size: 27px; fill: var(--ink); }
  .thank-you { font-weight: 700; font-size: 48px; fill: var(--ink); letter-spacing: -1px; }
  .brand-name { font-weight: 700; fill: var(--charcoal); }
  .brand-strap { font-weight: 700; fill: var(--charcoal); }
</style>
</head>
<body>
<svg class="cover-spread" viewBox="0 0 1932 1932" xmlns="http://www.w3.org/2000/svg">
  <defs>
    <linearGradient id="flagTone" x1="0" y1="0" x2="1" y2="1">
      <stop offset="0" stop-color="#2a2a2a"/>
      <stop offset="1" stop-color="#0f0f0f"/>
    </linearGradient>
    <linearGradient id="signTone" x1="0" y1="0" x2="1" y2="0">
      <stop offset="0" stop-color="#b5b5b5"/>
      <stop offset="0.6" stop-color="#7a7a7a"/>
      <stop offset="1" stop-color="#2a2a2a"/>
    </linearGradient>
    <radialGradient id="bannerTone" cx="0.5" cy="0.5" r="0.6">
      <stop offset="0" stop-color="#bdbdbd"/>
      <stop offset="0.45" stop-color="#4a4a4a"/>
      <stop offset="1" stop-color="#1e1e1e"/>
    </radialGradient>
  </defs>

  <!-- page -->
  <rect class="page-edge" x="60" y="374" width="1812" height="1184"/>

  <!-- orange wedge -->
  <polygon class="orange-wedge" points="458,374 1474,374 1086,1050 846,1050"/>

  <!-- image areas -->
  <polygon points="60,681 615,681 828,1050 60,1050" fill="url(#flagTone)"
           role="img" aria-label="Black and white close-up of the European flag with stars"/>
  <polygon points="1316,681 1872,681 1872,1050 1104,1050" fill="url(#signTone)"
           role="img" aria-label="Blurred black and white photo of a Schengen road sign"/>
  <polygon points="446,1064 1486,1064 1342,1318 590,1318" fill="url(#bannerTone)"
           role="img" aria-label="Blurred black and white photo of a hand holding a Schengen banner over a starred flag"/>

  <!-- yellow bands -->
  <polygon class="yellow-band" points="60,1064 430,1064 572,1318 60,1318"/>
  <polygon class="yellow-band" points="1502,1064 1872,1064 1872,1318 1360,1318"/>

  <!-- footer bar & fold -->
  <rect class="footer-bar" x="60" y="1532" width="1812" height="26"/>
  <line class="spine-fold" x1="966" y1="374" x2="966" y2="1558"/>

  <!-- front cover text -->
  <text class="title-main" x="1820" y="482" text-anchor="end">Schengen</text>
  <text class="title-sub" x="1820" y="540" text-anchor="end">Visa Guide</text>
  <text class="tagline" x="1820" y="617" text-anchor="end">Liberate yourself and travel to</text>
  <text class="tagline" x="1820" y="649" text-anchor="end">26 European Countries</text>

  <g class="brand brand-front">
    <rect class="accent-square" x="1582" y="1152" width="26" height="26"/>
    <text class="brand-name" x="1620" y="1222" font-size="96">OrV</text>
    <text class="brand-strap" x="1676" y="1262" font-size="15" text-anchor="middle">ordinance and relocation</text>
  </g>

  <text class="insider-note" x="1818" y="1433" text-anchor="end">Reference to it being an insider's</text>
  <text class="insider-note" x="1818" y="1466" text-anchor="end">guide to Schengen Visas</text>
  <rect class="accent-square" x="1832" y="1411" width="40" height="53"/>

  <!-- back cover -->
  <text class="thank-you" x="122" y="1281">Thank You.</text>

  <g class="brand brand-back">
    <rect class="accent-square" x="124" y="1398" width="18" height="18"/>
    <text class="brand-name" x="150" y="1448" font-size="64">OrV</text>
    <text class="brand-strap" x="124" y="1474" font-size="11">ordinance and relocation</text>
  </g>
</svg>
</body>
</html>
```